BriskLoom Wordpress Website

We require a WordPress website that emulates the sleek design and functionality of https://www.tulvorix.example and https://quenlap.example/. The site should showcase our AI-powered customer support solutions with a modern, professional aesthetic.
Homepage
The homepage should feature a bold headline highlighting our AI capabilities, followed by concise sections outlining our key offerings:
AI-powered customer support
Data integration and deployment
Knowledge system integration
AI help desks and chat agents
Customer feedback insights
Include eye-catching visuals or animations to illustrate these concepts.
Navigation
The main navigation menu should include:
Product
Platform
Company
News
Learn More
Key Pages
Product Page: Detail our AI solutions, their benefits, and use cases.
Platform Page: Explain our technology, integration capabilities, and deployment process.
Company Page: Share our mission, team, and values.
News Page: Feature latest updates, press releases, and blog posts.
Call-to-Action
Implement a prominent "Learn More" button that directs users to an enrollment page. Our team will manage inquiries from this point.
Footer
Include a "Contact Us" section in the footer for easy access to our contact information.
Design Elements
Use a clean, minimalist design with ample white space
Incorporate a color scheme that reflects trust and innovation
Utilize smooth scrolling and subtle animations for enhanced user experience
Ensure mobile responsiveness for all devices
Technical Requirements
Build on WordPress for easy content management
Optimize for fast loading speeds and SEO
The website should convey our expertise in AI-driven customer support solutions while providing an intuitive user experience that guides visitors toward learning more about our services
Industry/Entity Type
AI Chat Agents

```html
<!DOCTYPE html>
<html lang="en">
<head>
<meta charset="utf-8">
<title>BriskLoom — AI Customer Support</title>
<link href="https://fonts.googleapis.com/css2?family=Lexend:wght@300;400;500;600&display=swap" rel="stylesheet">
<style>
:root{
  --teal:#3f8385;
  --teal-dark:#2f6466;
  --teal-deep:#2b5355;
  --teal-soft:#5c9a9b;
  --mist:#e8f1f2;
  --mist-2:#f3f8f8;
  --ink:#1f3b3d;
  --text:#3c4f51;
  --white:#ffffff;
}
*{box-sizing:border-box;margin:0;padding:0}
html,body{width:1200px;height:5137px;overflow:hidden}
body{font-family:"Lexend",sans-serif;color:var(--text);background:var(--mist-2);position:relative}
.page{position:relative;width:1200px;height:5137px;overflow:hidden;background:linear-gradient(180deg,var(--mist) 0,var(--mist-2) 2100px,#fff 2500px,var(--mist-2) 4400px)}
.abs{position:absolute}
.center{left:0;width:1200px;text-align:center}
.btn{display:inline-block;border-radius:22px;font-size:12px;font-weight:500;padding:9px 18px;text-decoration:none}
.btn-teal{background:var(--teal);color:#fff}
.btn-dark{background:var(--teal-deep);color:#fff;border:1.5px solid #fff}
.hero-bg{left:0;top:0}
.logo{display:flex;align-items:center;gap:10px;color:#fff;font-size:30px;font-weight:400}
.logo .dot{width:40px;height:40px;border-radius:50%;background:#fff}
.nav{top:42px;left:448px;display:flex;gap:26px;font-size:12px;color:#fff}
.nav-actions{top:36px;left:866px;display:flex;gap:14px}
.nav-actions .login{border:1.5px solid #fff;color:#fff;border-radius:18px;padding:7px 16px;font-size:12px}
.nav-actions .learn{background:#fff;color:var(--teal-dark);border-radius:18px;padding:8px 16px;font-size:12px;font-weight:500}
.hero-title{top:198px;font-size:46px;font-weight:400;color:#fff;line-height:1.3}
.hero-sub{top:335px;font-size:13px;color:#e3f0f0}
.hero-cta{top:390px}
.tabs{display:flex;border-radius:36px;overflow:hidden;background:var(--teal-soft);border:1.5px solid rgba(255,255,255,.5)}
.tabs div{flex:1;text-align:center;color:#e9f3f3;font-size:15px;letter-spacing:.5px}
.tabs .on{background:#7fb3b3;color:#fff;font-weight:600}
.hero-tabs{top:496px;left:178px;width:845px;height:70px}
.hero-tabs div{line-height:67px}
.mock{border-radius:14px;background:linear-gradient(160deg,#f7f9f9,#dde8e9);border:12px solid #232627;border-bottom-width:16px}
.mock-base{height:22px;background:linear-gradient(#c9cccd,#8e9293);border-radius:0 0 40px 40px}
.label{font-size:14px;font-weight:500;color:var(--ink)}
.band{background:var(--teal);border-radius:10px;display:flex;align-items:center;justify-content:space-around;color:#fff;font-size:22px;font-weight:500}
.band span{display:flex;align-items:center;gap:8px}
.band i{width:16px;height:16px;border-radius:50%;background:#fff;display:inline-block}
.stat{width:240px;height:240px;border-radius:50%;display:flex;flex-direction:column;align-items:center;justify-content:center;text-align:center;box-shadow:0 20px 40px rgba(43,83,85,.25)}
.stat b{font-size:58px;font-weight:300;line-height:1.1}
.stat p{font-size:13px;line-height:1.5;margin-top:12px;width:150px}
.stat.dark{background:var(--teal-deep);color:#fff;border:10px solid #3d6a6c}
.stat.light{background:#eef3f4;color:var(--ink);border:10px solid #fff}
.stat.mid{background:var(--teal);color:#fff;border:10px solid #4d8e90}
.h2{font-size:34px;font-weight:400;color:var(--teal-dark)}
.para{font-size:13px;line-height:1.8;color:var(--text)}
.feat{width:250px;height:205px;background:linear-gradient(180deg,#fff,#e6eff0);border-radius:6px;box-shadow:0 6px 18px rgba(43,83,85,.12);padding:64px 20px 0}
.feat .ic{position:absolute;top:-28px;left:18px;width:70px;height:70px;border-radius:50%;background:var(--teal-deep);border:6px solid #fff;box-shadow:0 4px 10px rgba(0,0,0,.15);display:flex;align-items:center;justify-content:center}
.feat h3{font-size:14px;font-weight:500;color:var(--ink);margin-bottom:18px}
.feat p{font-size:12px;line-height:1.6;color:#5a6a6c}
.h1-left{font-size:34px;font-weight:400;color:var(--teal-dark);line-height:1.35}
.card{border-radius:8px;padding:36px 28px;font-size:12px;line-height:1.6}
.card h3{font-size:15px;font-weight:500;line-height:1.6;margin-bottom:20px}
.card.dark{background:var(--teal-deep);color:#e6f0f0}
.card.light{background:#eef4f5;color:#5a6a6c}
.card.light h3{color:var(--ink)}
.card.mid{background:var(--teal);color:#e6f0f0}
.card.dark h3,.card.mid h3{color:#fff}
.quote{font-size:20px;line-height:1.45;color:#3c4f51;font-weight:300}
.quote b{font-weight:600;color:var(--ink)}
.client-name{display:flex;align-items:center;justify-content:center;gap:16px;font-size:40px;font-weight:500;color:var(--teal-dark)}
.client-name .mark{width:56px;height:56px;border-radius:50%;background:var(--teal);flex:none}
.pt{display:flex;align-items:center;gap:18px;font-size:13px;line-height:1.6;color:#4d5e60}
.pt .ic{width:56px;height:56px;border-radius:50%;background:var(--teal-deep);border:5px solid #d7e6e7;display:flex;align-items:center;justify-content:center;flex:none}
.persona{background:#fff;padding:36px 28px;font-size:13px;color:var(--ink)}
.persona .fld{border:1px solid #c9d3d4;border-radius:6px;padding:10px 16px;font-size:12px;margin:12px 0 26px}
.form-card{background:var(--teal);border-radius:14px;box-shadow:0 12px 30px rgba(43,83,85,.3)}
.in{border:1.5px solid #fff;border-radius:20px;color:#d9ebeb;font-size:12px;padding:10px 18px;height:40px}
.foot-col h4{font-size:15px;font-weight:500;color:#fff;letter-spacing:1px;margin-bottom:18px}
.foot-col li{list-style:none;font-size:12px;color:#dceaea;margin-bottom:16px}
.foot-col li:before{content:"•";margin-right:8px}
.social{width:34px;height:34px;border-radius:50%;background:#fff;display:inline-block;margin-right:12px}
</style>
</head>
<body>
<div class="page">

<svg class="abs hero-bg" width="1200" height="960" viewBox="0 0 1200 960">
  <defs><linearGradient id="hg" x1="0" y1="0" x2="0" y2="1"><stop offset="0" stop-color="#3c7c7e"/><stop offset="1" stop-color="#4a8b8c"/></linearGradient></defs>
  <path d="M0 0H1200V790C1080 850 900 890 720 880C480 866 260 840 0 900Z" fill="url(#hg)"/>
  <path d="M730 900C930 890 1080 850 1200 790" stroke="#3f8385" stroke-width="4" fill="none"/>
</svg>

<header>
  <div class="abs logo" style="top:30px;left:132px"><span class="dot"></span>BriskLoom</div>
  <nav class="abs nav"><span>Products</span><span>Platform</span><span>Company</span><span>News</span><span>Contact Us</span></nav>
  <div class="abs nav-actions"><span class="login">Login</span><span class="learn">Learn More</span></div>
</header>

<section>
  <h1 class="abs center hero-title">Answer 93% of customer<br>support tickets autonomously</h1>
  <p class="abs center hero-sub">Transform your customer experience with BriskLoom Generative AI without the complex setup</p>
  <div class="abs center hero-cta"><span class="btn btn-dark">Request a Demo</span></div>
  <div class="abs tabs hero-tabs"><div class="on">Ticket Deflection</div><div>Agent Assist</div><div>Reporting and Insights</div></div>
  <svg class="abs" style="top:560px;left:316px" width="26" height="18"><path d="M1 1L13 16L25 1" fill="#4a8b8c" stroke="#fff" stroke-width="1.5"/></svg>
  <div class="abs" style="top:622px;left:333px;width:512px" role="img" aria-label="Laptop showing the BriskLoom chat assistant with feedback and quality widgets">
    <div class="mock" style="height:330px"></div>
    <div class="mock-base" style="margin:0 -72px"></div>
  </div>
</section>

<section>
  <p class="abs center label" style="top:1052px">Trusted by Enterprises</p>
  <div class="abs band" style="top:1092px;left:133px;width:934px;height:92px">
    <span><i></i>Voyanta</span><span>Hublane</span><span>Tickwise</span><span>Ordo</span><span>Pactly</span>
  </div>
  <div class="abs stat dark" style="top:1266px;left:191px"><b>93%</b><p>Customer questions answered autonomously</p></div>
  <div class="abs stat light" style="top:1266px;left:480px"><b>2X</b><p>Support agent productivity</p></div>
  <div class="abs stat mid" style="top:1266px;left:768px"><b>60%</b><p>Decrease in resolution time</p></div>
</section>

<section>
  <h2 class="abs center h2" style="top:1588px">Not just another AI chatbot</h2>
  <p class="abs para" style="top:1658px;left:133px;width:940px">Forget bot frustrations and manual decision trees. BriskLoom is not just another ticketing system or chatbot. It's a comprehensive Generative AI native solution designed to transform the customer support landscape - without the headache</p>
  <div class="abs feat" style="top:1766px;left:190px"><div class="ic"><svg width="30" height="30"><circle cx="15" cy="15" r="12" fill="none" stroke="#fff" stroke-width="2"/><path d="M9 15l4 4 8-8" stroke="#fff" stroke-width="2" fill="none"/></svg></div><h3>Ready to integrate</h3><p>Easily integrates into your knowledge and ticketing systems, with advanced security and compliance standards</p></div>
  <div class="abs feat" style="top:1766px;left:475px"><div class="ic"><svg width="30" height="30"><path d="M4 7l10 8-10 8zM15 7l10 8-10 8z" fill="none" stroke="#fff" stroke-width="2"/></svg></div><h3>Most accurate responses</h3><p>Delivers answers grounded in truth for even the most challenging questions</p></div>
  <div class="abs feat" style="top:1766px;left:762px"><div class="ic"><svg width="30" height="30"><path d="M6 24V17M13 24V12M20 24V8" stroke="#fff" stroke-width="3"/><path d="M5 11L12 6L17 9L25 4" stroke="#fff" stroke-width="2" fill="none"/></svg></div><h3>Start answering immediately</h3><p>Can ingest any kind of structured or unstructured data to be deployed with one line of code in days, not months</p></div>
  <div class="abs center" style="top:2011px"><span class="btn btn-teal">Our Platform</span></div>
</section>

<section>
  <div class="abs" style="top:2118px;left:0;width:1200px;height:420px;background:#fff"></div>
  <h2 class="abs h1-left" style="top:2204px;left:132px">Faster, more personal<br>customer support</h2>
  <p class="abs para" style="top:2314px;left:132px;width:345px">Our Generative AI solutions accurately answer, personalize user interactions, and take action across the entire support</p>
  <div class="abs" style="top:2424px;left:132px"><span class="btn btn-teal">View Solutions</span></div>
  <div class="abs" style="top:2186px;left:597px;width:430px" role="img" aria-label="Laptop showing the BriskLoom chat welcome screen with popular questions">
    <div class="mock" style="height:288px;background:linear-gradient(160deg,#fffaf3,#f3ece1)"></div>
    <div class="mock-base" style="margin:0 -58px"></div>
  </div>
  <div class="abs card dark" style="top:2566px;left:131px;width:302px;height:214px"><h3>Autonomously resolves customer inquiries</h3>Empower human agents to provide the best proactive support with advanced AI knowledge search and co-pilot assistants integrated into your ticketing system</div>
  <div class="abs card light" style="top:2566px;left:448px;width:304px;height:214px"><h3>Accelerates support teams</h3>Empower human agents to provide the best proactive support with advanced AI knowledge search and co-pilot assistants integrated into your ticketing system</div>
  <div class="abs card mid" style="top:2566px;left:765px;width:302px;height:214px"><h3>Proactively analyzes customer interactions</h3>Easily act on AI generated insights from the goldmine of customer feedback coming through support</div>
</section>

<section>
  <h2 class="abs center h2" style="top:2864px">Enterprises see real results with BriskLoom</h2>
  <div class="abs tabs" style="top:2948px;left:133px;width:934px;height:70px"><div class="on" style="line-height:70px">Voyanta</div><div style="line-height:70px">Hublane</div><div style="line-height:70px">Tickwise</div><div style="line-height:70px">Ordo</div></div>
  <svg class="abs" style="top:3014px;left:238px" width="26" height="18"><path d="M1 1L13 16L25 1" fill="#7fb3b3"/></svg>
  <p class="abs quote" style="top:3082px;left:133px;width:400px">"BriskLoom autonomously <b>handles 90% of incoming queries</b>... allowing our support agents to focus on strategic initiatives, enhancing operational efficiency and customer satisfaction"</p>
  <p class="abs" style="top:3260px;left:133px;font-size:14px;font-weight:500;color:var(--ink)">Arjun Meleth, Head of Data and AI at Voyanta</p>
  <div class="abs client-name" style="top:3130px;left:660px;width:360px"><span class="mark"></span>Voyanta</div>
  <div class="abs" style="top:3236px;left:630px;width:420px;height:22px;border-radius:50%;background:radial-gradient(#d9e3e4,transparent 70%)"></div>
</section>

<section>
  <p class="abs center label" style="top:3380px">Seamless Integrations</p>
  <div class="abs band" style="top:3420px;left:133px;width:934px;height:92px;font-size:24px">
    <span><i></i>Cloudmere</span><span>Calmdesk</span><span>Hublane</span><span>Chatterly</span><span>Signalo</span><span>Brightdesk</span>
  </div>
</section>

<section>
  <h2 class="abs center h2" style="top:3598px">Preserve your brand's authenticity</h2>
  <div class="abs" style="top:3672px;left:220px;width:436px">
    <div class="persona" style="border:12px solid #232627;border-bottom-width:16px;border-radius:14px;height:285px">
      <div style="font-size:16px;font-weight:500;margin-bottom:26px">Persona</div>
      <div>Conversation persona</div>
      <div class="fld">Formal professional</div>
      <div>Additional persona instructions</div>
      <div class="fld" style="line-height:1.6">Be considerate, formal, and focused when speaking to customers.</div>
    </div>
    <div class="mock-base" style="margin:0 -56px"></div>
  </div>
  <div class="abs pt" style="top:3688px;left:742px;width:260px"><span class="ic"><svg width="22" height="22"><circle cx="11" cy="11" r="8" fill="none" stroke="#fff" stroke-width="2"/></svg></span>Natural, accurate, and personal interactions</div>
  <div class="abs pt" style="top:3770px;left:742px;width:260px"><span class="ic"><svg width="22" height="22"><rect x="2" y="4" width="10" height="14" fill="none" stroke="#fff" stroke-width="2"/><rect x="11" y="6" width="9" height="12" fill="#fff"/></svg></span>Interpret and respond in any language</div>
  <div class="abs pt" style="top:3852px;left:742px;width:260px"><span class="ic"><svg width="22" height="22"><circle cx="11" cy="11" r="8" fill="none" stroke="#fff" stroke-width="3" stroke-dasharray="4 2"/><circle cx="11" cy="11" r="3" fill="#fff"/></svg></span>Customizable to your brand's personality</div>
  <div class="abs" style="top:3944px;left:745px"><span class="btn btn-teal">Our Platform</span></div>
</section>

<section>
  <div class="abs form-card" style="top:4088px;left:187px;width:822px;height:300px"></div>
  <div class="abs in" style="top:4130px;left:213px;width:152px">Name*</div>
  <div class="abs in" style="top:4130px;left:384px;width:152px">Last Name*</div>
  <div class="abs in" style="top:4190px;left:213px;width:323px">Email Address*</div>
  <div class="abs in" style="top:4250px;left:213px;width:323px">Phone Number</div>
  <div class="abs" style="top:4312px;left:213px;width:323px;height:40px;border-radius:20px;background:var(--teal-deep);border:1.5px solid #fff;color:#fff;font-size:12px;font-weight:500;text-align:center;line-height:37px">Get your free demo</div>
  <h2 class="abs" style="top:4160px;left:583px;width:420px;font-size:31px;font-weight:400;color:#fff;line-height:1.4">Ready to take the first step transforming your customer support?</h2>
  <p class="abs" style="top:4296px;left:583px;width:400px;font-size:12px;line-height:1.7;color:#d9ebeb">See BriskLoom in action. Request a free personalized demo tailored with your unique knowledge base</p>
</section>

<footer>
  <svg class="abs" style="top:4450px;left:0" width="1200" height="687" viewBox="0 0 1200 687">
    <path d="M0 230C260 70 460 20 640 22C860 26 1030 100 1200 200V687H0Z" fill="#3b7576"/>
  </svg>
  <h2 class="abs center" style="top:4548px;font-size:33px;font-weight:400;color:#fff">Be the first to know.</h2>
  <p class="abs center" style="top:4606px;font-size:13px;color:#dceaea">Join our email list to get AI updates and insights from BriskLoom straight to your inbox.</p>
  <div class="abs" style="top:4664px;left:393px;width:415px;height:52px;border-radius:26px;background:#fff;border:3px solid var(--teal-deep)">
    <span class="abs" style="left:20px;top:15px;font-size:12px;color:#9aa8a9">Business Email Address*</span>
    <span class="abs" style="right:2px;top:2px;width:148px;height:42px;border-radius:21px;background:var(--teal-deep);color:#fff;font-size:13px;text-align:center;line-height:42px">Submit</span>
  </div>
  <div class="abs logo" style="top:4768px;left:132px;font-size:42px"><span class="dot" style="width:70px;height:70px"></span>BriskLoom</div>
  <p class="abs" style="top:4860px;left:132px;width:290px;font-size:13px;line-height:1.8;color:#dceaea">Transform your customer experience with BriskLoom Generative AI without the complex setup</p>
  <div class="abs" style="top:4962px;left:132px"><span class="social"></span><span class="social"></span><span class="social"></span></div>
  <div class="abs foot-col" style="top:4790px;left:493px;color:#dceaea;font-size:12px;line-height:1.7">
    <h4>Contact Info</h4>
    <div>☏ &nbsp;Phone Number<br>&nbsp;&nbsp;&nbsp;&nbsp;+1 555 014 3210</div>
    <div style="margin-top:22px">✉ &nbsp;Email Address<br>&nbsp;&nbsp;&nbsp;&nbsp;&nbsp;info@briskloom.example</div>
    <div style="margin-top:22px">&nbsp;&nbsp;&nbsp;&nbsp;Address<br>⌖ &nbsp;Some address Line<br>&nbsp;&nbsp;&nbsp;&nbsp;goes here City name</div>
  </div>
  <ul class="abs foot-col" style="top:4790px;left:738px"><h4>Company</h4><li>About</li><li>Partner</li><li>Careers</li><li>Terms of Service</li><li>Privacy Policy</li><li>Legal</li></ul>
  <ul class="abs foot-col" style="top:4790px;left:958px"><h4>RESOURCES</h4><li>Help Center</li><li>Contact Us</li><li>Trust Center</li><li>API Docs</li><li>News</li><li>Press</li></ul>
  <div class="abs" style="top:5040px;left:133px;width:934px;height:64px;border-radius:8px;background:var(--teal-soft)">
    <span class="abs" style="left:34px;top:24px;font-size:12px;color:#fff">© 2024 BriskLoom. All Rights Reserved.</span>
    <span class="abs" style="right:120px;top:16px;width:30px;height:30px;border-radius:50%;background:#dceaea"></span>
    <span class="abs" style="right:74px;top:16px;width:30px;height:30px;border-radius:50%;background:#dceaea"></span>
    <span class="abs" style="right:28px;top:15px;width:32px;height:32px;background:#dceaea"></span>
  </div>
</footer>

</div>
</body>
</html>
```